Elegant Business Card for Technology Company

Client is a supplier of innovative industrial communications and automation equipment since 2002. This contest is to gather fresh ideas for a redesign of the existing business card. Client is looking for design that best communicates tagline "Industrial Networking and Computing Specialist".

Design submissions should look modern, clean, elegant and professional. It should not be cluttered. Use white as the primary colour. Orange and black as secondary colour. Refer to jpeg File 1 on the current design.

Fonts used by Client used include Arial Regular, Arial Black, Roboto Regular, Roboto Black and Lato.

The winning design will be sent for offset printing using super white 250gsm artcard paper (open for suggestions).

Target Market(s)

System Engineers, Project Managers, Purchasing Managers from companies providing engineering services for Smart Cities.

Industry/Entity Type

Information Technology

Contact Information for Business Card

Refer to PDF File 3 for Business Card Details. Priority of short contact information would be as follows Name > Job Title > Email > Mobile > Web > Tel > Fax > Business Address >UEN (UEN represents company registration number)

Font styles to use
Sans Serif

Colors
ffffff
f37122
000000
5c5c5c

Requirements
Must have
• Refer to AI File 2 (Company Logo) & PDF File 3 (Information on Namecard)
Should not have
• No QR codes
• No Social Media Icons
• Do not create full Black or Orange colour background

```html
<!DOCTYPE html>
<html lang="en">
<head>
<meta charset="utf-8">
<title>Korvane Business Card</title>
<link rel="stylesheet" href="https://fonts.googleapis.com/css2?family=Roboto:wght@400;500;700;900&display=swap">
<style>
  :root {
    --white: #ffffff;
    --orange: #f37122;
    --black: #000000;
    --grey: #5c5c5c;
    --backdrop: #e9e9e9;
  }
  * { box-sizing: border-box; margin: 0; padding: 0; }
  html, body {
    width: 1200px; height: 900px; overflow: hidden;
    background: var(--backdrop);
    font-family: "Roboto", Arial, sans-serif;
    color: var(--black);
  }
  .stage { position: relative; width: 1200px; height: 900px; }
  .card {
    position: absolute;
    width: 680px; height: 389px;
    background: var(--white);
    border-radius: 22px;
    box-shadow: 0 10px 30px rgba(0,0,0,0.15);
    overflow: hidden;
  }
  .card--front { left: 120px; top: 40px; }
  .card--back { left: 400px; top: 471px; }

  .wordmark {
    position: absolute;
    display: flex; align-items: center; gap: 14px;
  }
  .wordmark__dot {
    width: 58px; height: 58px; border-radius: 50%;
    background: var(--orange);
  }
  .wordmark__name {
    font-weight: 900; color: var(--black);
    letter-spacing: 1px; line-height: 1;
  }

  /* Front */
  .card--front .wordmark { left: 150px; top: 74px; }
  .card--front .wordmark__name { font-size: 50px; }
  .front__rule {
    position: absolute; height: 2px; background: var(--orange);
  }
  .front__rule--top { left: 330px; right: 0; top: 150px; }
  .front__rule--bottom { left: 110px; right: 0; top: 330px; }
  .front__text {
    position: absolute; left: 150px; width: 400px; top: 172px;
    text-align: center;
  }
  .tagline {
    font-size: 15px; font-weight: 500; letter-spacing: 0.4px;
    text-transform: uppercase; margin-bottom: 8px;
  }
  .services { list-style: none; font-size: 15px; line-height: 20px; }
  .services__item--accent { color: var(--orange); }

  /* Back */
  .card--back .wordmark { left: 40px; top: 44px; }
  .card--back .wordmark__dot { width: 50px; height: 50px; }
  .card--back .wordmark__name { font-size: 42px; }
  .company {
    position: absolute; left: 40px; top: 118px;
    font-size: 16px; line-height: 20px; text-transform: uppercase;
  }
  .company__accent { color: var(--orange); font-weight: 700; }
  .company__label { color: var(--orange); text-transform: none; }
  .back__rule {
    position: absolute; left: 100px; right: 40px; top: 188px;
    height: 2px; background: var(--black);
  }
  .person {
    position: absolute; right: 40px; top: 126px; text-align: right;
  }
  .person__name { font-size: 22px; font-weight: 900; text-transform: uppercase; line-height: 1.1; }
  .person__title { font-size: 14px; color: var(--orange); text-transform: uppercase; letter-spacing: 0.5px; }
  .contacts {
    position: absolute; right: 40px; top: 202px;
    list-style: none; font-size: 15px; line-height: 21px; text-align: right;
  }
  .contacts__item { display: flex; justify-content: flex-end; align-items: center; gap: 8px; }
  .contacts__icon { width: 12px; height: 12px; fill: none; stroke: var(--orange); stroke-width: 1.6; }
  .address {
    position: absolute; left: 40px; bottom: 40px;
    font-size: 15px; font-weight: 500; line-height: 20px;
  }
</style>
</head>
<body>
<main class="stage">

  <section class="card card--front" aria-label="Card front">
    <div class="wordmark">
      <span class="wordmark__dot"></span>
      <span class="wordmark__name">KORVANE</span>
    </div>
    <span class="front__rule front__rule--top"></span>
    <div class="front__text">
      <p class="tagline">Industrial Networking and Computing Specialist</p>
      <ul class="services">
        <li class="services__item">Industrial Ethernet / Wireless / Cellular</li>
        <li class="services__item services__item--accent">Industrial and Embedded Computing</li>
        <li class="services__item">Serial / Fieldbus Connectivity</li>
        <li class="services__item services__item--accent">IP Video Surveillance</li>
        <li class="services__item">Remote Automation</li>
      </ul>
    </div>
    <span class="front__rule front__rule--bottom"></span>
  </section>

  <section class="card card--back" aria-label="Card back">
    <div class="wordmark">
      <span class="wordmark__dot"></span>
      <span class="wordmark__name">KORVANE</span>
    </div>
    <p class="company">
      <span class="company__accent">Korvane</span> Asia Pacific Pte Ltd<br>
      <span class="company__label">UEN No.</span> 200412345K
    </p>

    <div class="person">
      <p class="person__name">Daniel Wong</p>
      <p class="person__title">Sales Manager</p>
    </div>
    <span class="back__rule"></span>

    <ul class="contacts">
      <li class="contacts__item">+65 8123 4567
        <svg class="contacts__icon" viewBox="0 0 12 12"><rect x="3" y="1" width="6" height="10" rx="1"/><line x1="5" y1="9" x2="7" y2="9"/></svg></li>
      <li class="contacts__item">+65 6123 4560
        <svg class="contacts__icon" viewBox="0 0 12 12"><path d="M2 2l2.5-.5 1.2 2.6-1.4 1a6 6 0 0 0 2.6 2.6l1-1.4 2.6 1.2L10 10C5.5 10 2 6.5 2 2z"/></svg></li>
      <li class="contacts__item">+65 6123 4561
        <svg class="contacts__icon" viewBox="0 0 12 12"><rect x="1.5" y="5" width="9" height="5" rx="1"/><rect x="3.5" y="1.5" width="5" height="3.5"/></svg></li>
      <li class="contacts__item">sales@korvane.com.sg
        <svg class="contacts__icon" viewBox="0 0 12 12"><rect x="1.5" y="2.5" width="9" height="7" rx="1"/><path d="M1.5 3l4.5 3.5L10.5 3"/></svg></li>
      <li class="contacts__item">www.korvane.com.sg
        <svg class="contacts__icon" viewBox="0 0 12 12"><circle cx="6" cy="6" r="4.5"/><line x1="1.5" y1="6" x2="10.5" y2="6"/><ellipse cx="6" cy="6" rx="2" ry="4.5"/></svg></li>
    </ul>

    <p class="address">21 Kestrel Crescent Techpark #04-12<br>(Lobby B), Singapore 401234</p>
  </section>

</main>
</body>
</html>
```